Real estate website

Please find attached a rough outline of what we want for the design. This is just for placement to show what to have on the menu's as content, etc. but please make it look much more professional.
Please make the bottom footer a similar gradient to the logo
Please make the sign up now and log in buttons look better - these are just samples to show placement
Please use the correct logos for dwelloria.com.au, plotnex.com.au and roofquill.com.au
Where it has 'video embed' just leave that as is as we will replace that with a video.

```html
<!DOCTYPE html>
<html lang="en">
<head>
<meta charset="utf-8">
<title>Listara – Sell with no commission</title>
<link href="https://fonts.googleapis.com/css2?family=Poppins:wght@300;400;500;600;700&display=swap" rel="stylesheet">
<style>
:root{
  --black:#000;
  --white:#fff;
  --ink:#111;
  --green-dark:#0b6b34;
  --green-mid:#2f8f2f;
  --green-light:#86c92a;
  --red:#c8102e;
  --grey-line:#cfd3d6;
  --sky-top:#eef2f6;
  --sky-mid:#dfe5ea;
  --roof:#c8533f;
}
*{box-sizing:border-box;margin:0;padding:0}
html,body{width:1200px;height:675px;overflow:hidden}
body{font-family:"Poppins",sans-serif;color:var(--ink);background:var(--white);position:relative}
.hero-bg{position:absolute;inset:0;background:
  radial-gradient(ellipse at 50% 35%,rgba(255,255,255,.95) 0%,rgba(255,255,255,.7) 35%,rgba(255,255,255,0) 70%),
  linear-gradient(180deg,var(--sky-top) 0%,var(--sky-mid) 55%,#c9cfd4 100%)}
.site-header{position:absolute;left:93px;top:0;width:1006px;height:71px;background:var(--black);border-radius:0 0 14px 14px;display:flex;align-items:center;padding:0 34px 0 31px}
.brand{display:flex;align-items:center;gap:10px;color:var(--white);font-size:20px;font-weight:400}
.brand-dot{width:18px;height:18px;border-radius:50%;background:var(--green-light)}
.main-nav{margin-left:auto;display:flex;gap:15px;font-size:9.5px;font-weight:500;color:var(--white)}
.auth{display:flex;gap:9px;margin-left:49px}
.btn-pill{height:23px;border-radius:12px;display:flex;align-items:center;justify-content:center;font-size:8.5px;font-weight:600;width:78px}
.btn-signup{background:linear-gradient(90deg,var(--green-dark),var(--green-light));color:var(--white)}
.btn-login{background:var(--white);color:var(--green-dark)}
.wordmark{position:absolute;left:400px;top:128px;font-size:80px;font-weight:300;letter-spacing:1px;line-height:1;display:flex;align-items:center;gap:22px}
.wordmark-mark{width:46px;height:46px;background:linear-gradient(135deg,var(--green-dark),var(--green-light))}
.pitch{position:absolute;left:463px;top:242px;font-size:24px;font-weight:600}
.listing-sites{position:absolute;left:465px;top:292px;list-style:none}
.listing-sites li{display:flex;align-items:center;gap:14px;height:40px}
.listing-sites svg{width:24px;height:24px}
.site-name{font-size:14px;font-weight:600;color:var(--ink)}
.offer{position:absolute;left:459px;top:429px;font-size:17px;line-height:23px}
.phone{display:inline-block;background:var(--red);color:var(--white);font-weight:600;border-radius:10px;padding:0 5px;line-height:19px;letter-spacing:.5px}
.blurb{position:absolute;left:459px;top:490px;width:305px;font-size:9.3px;line-height:15px}
.video-card{position:absolute;left:93px;top:290px;width:304px;height:257px;background:var(--white);border:2px solid var(--green-mid);border-radius:12px}
.video-frame{position:absolute;left:10px;top:9px;width:281px;height:190px;background:linear-gradient(180deg,#d2d2d2,#c4c4c4)}
.video-controls{position:absolute;left:40px;top:218px;width:240px;height:22px;display:flex;align-items:center}
.track{position:relative;width:186px;height:2px;background:var(--grey-line)}
.track-fill{position:absolute;left:0;top:0;width:88px;height:2px;background:var(--green-mid)}
.knob{position:absolute;left:77px;top:-11px;width:23px;height:23px;border-radius:50%;background:var(--green-mid);display:flex;align-items:center;justify-content:center}
.time{margin-left:9px;font-size:12.5px;color:#333}
.guide-form{position:absolute;left:846px;top:154px;width:254px;height:371px;background:rgba(255,255,255,.85);border:1px solid #c9c9c9;border-radius:14px;text-align:center}
.guide-form h2{margin-top:22px;font-size:20.5px;font-weight:700}
.guide-form .sub{font-size:9.5px;color:var(--green-dark);margin-top:2px}
.field{display:block;margin:0 auto 9px 36px;width:181px;height:30px;border:1px solid #9a9a9a;border-radius:15px;background:var(--white);font-family:inherit;font-size:9px;padding:0 14px;color:#888}
.fields{margin-top:19px}
.captcha{margin:12px auto 0;width:127px;height:31px;display:flex;border:1px solid #ccc}
.captcha-left{flex:1;background:#3c78e0}
.captcha-right{width:35px;background:#eee}
.submit{margin:17px auto 0;width:118px;height:38px;border-radius:19px;border:2px solid var(--white);background:linear-gradient(90deg,var(--green-dark),var(--green-light));color:var(--white);font-family:inherit;font-size:11.5px;font-weight:600;letter-spacing:1px;display:flex;align-items:center;justify-content:center}
.services-bar{position:absolute;left:93px;top:604px;width:1006px;height:80px;background:linear-gradient(90deg,var(--green-dark),var(--green-light));border-radius:14px 14px 0 0;border:2px solid var(--white);display:flex;justify-content:center;gap:25px;padding-top:27px;color:var(--white);font-size:13.5px}
</style>
</head>
<body>
<div class="hero-bg" role="img" aria-label="Photo of white suburban houses with red tiled roofs"></div>

<header class="site-header">
  <div class="brand"><span class="brand-dot"></span>Listara</div>
  <nav class="main-nav"><span>Sell My Property</span><span>Rent My Property</span><span>Rental Management</span></nav>
  <div class="auth"><span class="btn-pill btn-signup">Sign up Now</span><span class="btn-pill btn-login">Log in</span></div>
</header>

<div class="wordmark"><span class="wordmark-mark"></span>Listara</div>

<h1 class="pitch">Sell with no commission on</h1>
<ul class="listing-sites">
  <li><svg viewBox="0 0 24 24" fill="none" stroke="#111" stroke-width="1.8" stroke-linecap="round"><path d="M20 11a9 9 0 1 1-4-7"/><path d="M8 12l4 4 9-10"/></svg><span class="site-name">dwelloria.com.au</span></li>
  <li><svg viewBox="0 0 24 24" fill="none" stroke="#111" stroke-width="1.8" stroke-linecap="round"><path d="M20 11a9 9 0 1 1-4-7"/><path d="M8 12l4 4 9-10"/></svg><span class="site-name">plotnex.com.au</span></li>
  <li><svg viewBox="0 0 24 24" fill="none" stroke="#111" stroke-width="1.8" stroke-linecap="round"><path d="M20 11a9 9 0 1 1-4-7"/><path d="M8 12l4 4 9-10"/></svg><span class="site-name">roofquill.com.au</span></li>
</ul>

<p class="offer">Want to Pay Nothing Upfront?<br>Ask us How - <span class="phone">0491570110</span></p>
<p class="blurb">Listing a house in Australia tempus sed malesuada sed, imperdiet quis eros. Maecenas tincidunt augue suscipit enim varius, ut pretium neque blandit. Phasellus erat tortor and get started.</p>

<div class="video-card">
  <div class="video-frame" role="img" aria-label="Video embed placeholder: presenter in a suit"></div>
  <div class="video-controls">
    <div class="track"><div class="track-fill"></div>
      <div class="knob"><svg width="8" height="9" viewBox="0 0 8 9"><path d="M1 0l7 4.5L1 9z" fill="#fff"/></svg></div>
    </div>
    <span class="time">2:05:49</span>
  </div>
</div>

<form class="guide-form">
  <h2>Get Your Free Guide</h2>
  <p class="sub">To listing privately in the ACT</p>
  <div class="fields">
    <input class="field" placeholder="Email *">
    <input class="field" placeholder="First name *">
    <input class="field" placeholder="Last name *">
    <input class="field" placeholder="Phone number">
  </div>
  <div class="captcha"><div class="captcha-left"></div><div class="captcha-right"></div></div>
  <div class="submit">Submit</div>
</form>

<footer class="services-bar">
  <span>Finance</span><span>-</span><span>Conveyancing</span><span>-</span><span>Building Inspection</span><span>-</span><span>Pest Inspection</span><span>-</span><span>Valuation</span><span>-</span><span>Market Appraisal</span>
</footer>
</body>
</html>
```